Verpackungsdesign für neues Kakteen Anzuchtset
Zielgruppe
Wir sind ein eCommerce StartUp aus Deutschland, mit Schwerpunkt Samen, Anzuchtsets und Zubehör. Unsere Zielgruppe findet sich in pflanzenaffinen Kunden*innen und im Bereich der Geschenke-Suchenden für Jung und Alt.
Wir suchen für unser neues Kakteen Anzuchtset ein 'Eyecatcher Design' auf der vorgegebenen Verpackung.
Aufgabenstellung
Es gibt auf diversen Marktplätzen bereits Anbieter die ähnliche Sets anbieten. Das Design soll also in jedem Fall auffallen um nicht beim Scrollen einfach unterzugehen. Unser Logo (beigefügt) soll sich auf unserer Verpackung wiederfinden. Wir vertreiben bereits Bonsai Starter Kits, das Design soll aber nicht an diese Sets angelehnt sein. (Die Inhalte des Sets sehen Sie in den Bildern) Wir haben bereits Stockbilder gekauft, die auf der Verpackung die jeweilige Sorte der Kakteen zeigen soll. Sollten andere Bilder genutzt werden, dann bitten wir um Rückmeldung. Auch das Template für die Verpackung ist in den Anhängen zu finden.
Es wird 2 Varianten der Anzuchtsets geben, das Design soll bei beiden gleich sein, nur die Bilder der Kakteen, der EAN Code und die Anleitung der Anzucht unterscheidet sich. Auch die Anleitung der einzelnen Sorten ist beigefügt. Ebenfalls beigefügt ist das Design der Samenkarten welche dem Set beigefügt sind (dort sind die Samen aufgebracht.)
1. Set: Madagascar Palme + Echter Tigerrachen + Mini-Gewächshaus, Markierer und Anzuchtkarte
2. Set: Wüstenrose + Lebender Granit + Mini Gewächshaus, Markierer und Anzuchtkarte
Eine Illustrierte Anleitung ist ebenfalls beigefügt und kann genutzt werden.
Falls Fragen offen sind, dann melden Sie sich gerne.

```html
<!DOCTYPE html>
<html lang="de">
<head>
<meta charset="utf-8">
<title>Sprosslabor – Kakteen Anzuchtset, Druckdaten</title>
<link href="https://fonts.googleapis.com/css2?family=Amatic+SC:wght@400;700&family=Caveat:wght@500&display=swap" rel="stylesheet">
<style>
  :root {
    --canvas: #d9d9d9;
    --board: #ffffff;
    --cut-line: #c4c4c4;
    --ink: #3a3a3a;
    --ink-soft: #6b6b6b;
    --leaf: #7fa35a;
  }
  html, body {
    margin: 0;
    width: 822px;
    height: 1200px;
    overflow: hidden;
    background: var(--canvas);
  }
  .dieline {
    position: absolute;
    left: 51px;
    width: 719px;
    height: 558px;
  }
  .dieline--set-one { top: 28px; }
  .dieline--set-two { top: 614px; }
  .cut { fill: var(--board); stroke: var(--cut-line); stroke-width: 0.8; }
  .frame { fill: none; stroke: var(--ink); stroke-width: 0.6; }
  .pill { fill: var(--board); stroke: var(--ink); stroke-width: 0.5; }
  .caps { font-family: "Amatic SC", sans-serif; fill: var(--ink); }
  .script { font-family: "Caveat", cursive; fill: var(--ink); }
  .brand { font-family: "Amatic SC", sans-serif; fill: var(--ink-soft); font-weight: 400; }
  .brand-dot { fill: none; stroke: var(--ink-soft); stroke-width: 0.6; }
  .badge { fill: var(--board); stroke: var(--ink-soft); stroke-width: 0.5; }
  .fine { font-family: "Amatic SC", sans-serif; fill: var(--ink); font-size: 4.4px; }
  .fine-head { font-family: "Amatic SC", sans-serif; fill: var(--ink); font-size: 4.6px; font-weight: 700; }
  .tag { font-family: "Amatic SC", sans-serif; fill: var(--ink-soft); font-size: 5px; font-weight: 700; }
</style>
</head>
<body>

<svg class="dieline dieline--set-one" viewBox="0 0 625 485" role="group" aria-label="Faltschachtel Set 1: Madagascar Palme und Echter Tigerrachen">
  <defs>
    <radialGradient id="tone-palm">
      <stop offset="0" stop-color="#fbfbf6"/>
      <stop offset="0.35" stop-color="#e8eee0"/>
      <stop offset="0.6" stop-color="#6f9a55"/>
      <stop offset="0.85" stop-color="#3f6b3a" stop-opacity="0.6"/>
      <stop offset="1" stop-color="#3f6b3a" stop-opacity="0"/>
    </radialGradient>
    <radialGradient id="tone-tiger">
      <stop offset="0" stop-color="#f3e75e"/>
      <stop offset="0.4" stop-color="#e0d342"/>
      <stop offset="0.68" stop-color="#86ab5c"/>
      <stop offset="0.88" stop-color="#9c8664" stop-opacity="0.6"/>
      <stop offset="1" stop-color="#9c8664" stop-opacity="0"/>
    </radialGradient>
    <radialGradient id="tone-rose">
      <stop offset="0" stop-color="#b8b7ae"/>
      <stop offset="0.3" stop-color="#6f9558"/>
      <stop offset="0.55" stop-color="#e47aa0"/>
      <stop offset="0.78" stop-color="#b0653c" stop-opacity="0.7"/>
      <stop offset="1" stop-color="#b0653c" stop-opacity="0"/>
    </radialGradient>
    <radialGradient id="tone-granite">
      <stop offset="0" stop-color="#f0a43c"/>
      <stop offset="0.35" stop-color="#e3832f"/>
      <stop offset="0.6" stop-color="#4d6660"/>
      <stop offset="0.85" stop-color="#3f524e" stop-opacity="0.6"/>
      <stop offset="1" stop-color="#3f524e" stop-opacity="0"/>
    </radialGradient>
    <radialGradient id="tone-guide">
      <stop offset="0" stop-color="#a9c98a"/>
      <stop offset="0.5" stop-color="#d9cbb0"/>
      <stop offset="1" stop-color="#efe6d6" stop-opacity="0"/>
    </radialGradient>
    <radialGradient id="tone-cards">
      <stop offset="0" stop-color="#9fb27c"/>
      <stop offset="0.6" stop-color="#d2b98f"/>
      <stop offset="1" stop-color="#d2b98f" stop-opacity="0"/>
    </radialGradient>

    <g id="box-net">
      <path class="cut" d="M0 162 L27 150 L27 400 L0 388 Z"/>
      <path class="cut" d="M27 150 L27 40 Q27 0 70 0 L172 0 Q215 0 215 40 L215 150 Z"/>
      <path class="cut" d="M215 150 L228 75 L302 75 L325 150 Z"/>
      <path class="cut" d="M515 150 L528 75 L602 75 L625 150 Z"/>
      <rect class="cut" x="27" y="150" width="598" height="250"/>
      <line class="cut" x1="215" y1="150" x2="215" y2="400"/>
      <line class="cut" x1="325" y1="150" x2="325" y2="400"/>
      <line class="cut" x1="515" y1="150" x2="515" y2="400"/>
      <path class="cut" d="M27 400 L215 400 L200 445 L175 445 L160 485 L82 485 L67 445 L42 445 Z"/>
      <path class="cut" d="M215 400 L325 400 L312 440 L228 440 Z"/>
      <path class="cut" d="M325 400 L515 400 L500 445 L475 445 L460 485 L380 485 L365 445 L340 445 Z"/>
      <path class="cut" d="M515 400 L625 400 L612 440 L528 440 Z"/>
      <g transform="rotate(180 121 85)">
        <circle class="brand-dot" cx="84" cy="85" r="6"/>
        <text class="brand" x="95" y="90" font-size="15">Sprosslabor</text>
      </g>
    </g>

    <g id="guide-panel">
      <text class="tag" x="8" y="14">INHALT</text>
      <ellipse cx="55" cy="44" rx="50" ry="26" fill="url(#tone-guide)" role="img" aria-label="Zeichnung des Setinhalts: Samenkarte, Mini-Gewächshaus, Markierer"/>
      <text class="tag" x="8" y="82">GRATIS</text>
      <circle cx="55" cy="112" r="26" fill="none" stroke="var(--leaf)" stroke-width="0.5"/>
      <ellipse cx="55" cy="112" rx="24" ry="22" fill="url(#tone-cards)" role="img" aria-label="Abbildung der beiliegenden Bonsai-Samenkarten"/>
      <text class="tag" x="8" y="154">SO GEHT'S</text>
      <ellipse cx="55" cy="200" rx="50" ry="40" fill="url(#tone-guide)" role="img" aria-label="Illustrierte Anleitung: Karte einlegen, bewässern, Deckel aufsetzen"/>
    </g>
  </defs>

  <use href="#box-net"/>

  <g id="front-set-one">
    <rect class="frame" x="35" y="165" width="170" height="220"/>
    <rect class="pill" x="70" y="160" width="100" height="10"/>
    <text class="caps" x="120" y="168" font-size="7.5" text-anchor="middle">(PACHYPODIUM LAMEREI)</text>
    <text class="script" x="46" y="192" font-size="19">Madagascar</text>
    <text class="script" x="118" y="210" font-size="19">Palme</text>
    <ellipse cx="88" cy="258" rx="56" ry="50" fill="url(#tone-palm)" role="img" aria-label="Illustration: Madagascar Palme mit weißen Blüten"/>
    <ellipse cx="148" cy="300" rx="52" ry="42" fill="url(#tone-tiger)" role="img" aria-label="Illustration: gelb blühender Echter Tigerrachen auf Erde"/>
    <circle class="badge" cx="200" cy="235" r="22"/>
    <text class="caps" x="200" y="226" font-size="4.6" text-anchor="middle">+MINI-GEWÄCHSHAUS,</text>
    <text class="caps" x="200" y="232" font-size="4.6" text-anchor="middle">MARKIERER UND</text>
    <text class="caps" x="200" y="238" font-size="4.6" text-anchor="middle">ANZUCHTKARTE</text>
    <text class="caps" x="200" y="249" font-size="9" text-anchor="middle">DAZU</text>
    <text class="script" x="70" y="352" font-size="17">Echter</text>
    <text class="script" x="92" y="372" font-size="17">Tigerrachen</text>
    <circle class="brand-dot" cx="45" cy="366" r="3"/>
    <text class="brand" x="50" y="368" font-size="6">Sprosslabor</text>
    <rect class="pill" x="82" y="380" width="76" height="10"/>
    <text class="caps" x="120" y="388" font-size="7.5" text-anchor="middle">(FAUCARIA TIGRINA)</text>
  </g>
  <use href="#guide-panel" x="215" y="150"/>
  <use href="#front-set-one" x="300"/>

  <g transform="translate(515 150)">
    <text class="script" x="6" y="16" font-size="10">Madagascar Palme</text>
    <text class="fine" x="72" y="16">(Pachypodium lamerei)</text>
    <text class="fine-head" x="6" y="28">AUSSAAT</text>
    <text class="fine" x="6" y="34">Samen einen Tag in lauwarmem</text>
    <text class="fine" x="6" y="39">Wasser quellen lassen, dann flach</text>
    <text class="fine" x="6" y="44">auf die Anzuchtkarte legen.</text>
    <text class="fine-head" x="6" y="54">KEIMUNG</text>
    <text class="fine" x="6" y="60">Bei 24 Grad keimen die Samen</text>
    <text class="fine" x="6" y="65">nach etwa zwei bis drei Wochen.</text>
    <text class="fine-head" x="6" y="75">STANDORT</text>
    <text class="fine" x="6" y="81">Hell und warm, ohne pralle</text>
    <text class="fine" x="6" y="86">Mittagssonne am Fensterplatz.</text>
    <text class="script" x="6" y="106" font-size="10">Echter Tigerrachen</text>
    <text class="fine" x="76" y="106">(Faucaria tigrina)</text>
    <text class="fine-head" x="6" y="118">AUSSAAT</text>
    <text class="fine" x="6" y="124">Samen nur leicht andrücken, nicht</text>
    <text class="fine" x="6" y="129">mit Erde bedecken.</text>
    <text class="fine-head" x="6" y="139">KEIMUNG</text>
    <text class="fine" x="6" y="145">Deckel geschlossen halten, bis</text>
    <text class="fine" x="6" y="150">die ersten Blättchen erscheinen.</text>
    <text class="fine-head" x="6" y="160">PFLEGE</text>
    <text class="fine" x="6" y="166">Sparsam gießen, Staunässe</text>
    <text class="fine" x="6" y="171">unbedingt vermeiden.</text>
    <text class="fine" x="6" y="232">Sprosslabor GmbH · Musterweg 12 · 10115 Berlin</text>
    <circle class="brand-dot" cx="92" cy="240" r="2.5"/>
    <text class="brand" x="64" y="242" font-size="5">Sprosslabor</text>
  </g>
</svg>

<svg class="dieline dieline--set-two" viewBox="0 0 625 485" role="group" aria-label="Faltschachtel Set 2: Wüstenrose und Lebender Granit">
  <use href="#box-net"/>

  <g id="front-set-two">
    <rect class="frame" x="35" y="165" width="170" height="220"/>
    <rect class="pill" x="78" y="160" width="84" height="10"/>
    <text class="caps" x="120" y="168" font-size="7.5" text-anchor="middle">(ADENIUM OBESUM)</text>
    <text class="script" x="64" y="196" font-size="20">Wüstenrose</text>
    <ellipse cx="108" cy="258" rx="68" ry="48" fill="url(#tone-rose)" role="img" aria-label="Illustration: blühende Wüstenrose in verzierter Tonschale"/>
    <ellipse cx="156" cy="306" rx="44" ry="38" fill="url(#tone-granite)" role="img" aria-label="Illustration: orange blühender Lebender Granit"/>
    <circle class="badge" cx="200" cy="235" r="22"/>
    <text class="caps" x="200" y="226" font-size="4.6" text-anchor="middle">+MINI-GEWÄCHSHAUS,</text>
    <text class="caps" x="200" y="232" font-size="4.6" text-anchor="middle">MARKIERER UND</text>
    <text class="caps" x="200" y="238" font-size="4.6" text-anchor="middle">ANZUCHTKARTE</text>
    <text class="caps" x="200" y="249" font-size="9" text-anchor="middle">DAZU</text>
    <text class="script" x="76" y="352" font-size="17">Lebender</text>
    <text class="script" x="112" y="372" font-size="17">Granit</text>
    <circle class="brand-dot" cx="45" cy="366" r="3"/>
    <text class="brand" x="50" y="368" font-size="6">Sprosslabor</text>
    <rect class="pill" x="84" y="380" width="72" height="10"/>
    <text class="caps" x="120" y="388" font-size="7.5" text-anchor="middle">(PLEIOSPILOS NELII)</text>
  </g>
  <use href="#guide-panel" x="215" y="150"/>
  <use href="#front-set-two" x="300"/>

  <g transform="translate(515 150)">
    <text class="script" x="6" y="16" font-size="10">Wüstenrose</text>
    <text class="fine" x="56" y="16">(Adenium obesum)</text>
    <text class="fine-head" x="6" y="28">AUSSAAT</text>
    <text class="fine" x="6" y="34">Samen flach auf feuchtes Substrat</text>
    <text class="fine" x="6" y="39">legen und leicht andrücken.</text>
    <text class="fine-head" x="6" y="49">KEIMUNG</text>
    <text class="fine" x="6" y="55">Nach ein bis zwei Wochen zeigen</text>
    <text class="fine" x="6" y="60">sich die ersten Keimlinge.</text>
    <text class="fine-head" x="6" y="70">STANDORT</text>
    <text class="fine" x="6" y="76">Warm bei mindestens 22 Grad,</text>
    <text class="fine" x="6" y="81">hell und geschützt.</text>
    <text class="script" x="6" y="106" font-size="10">Lebender Granit</text>
    <text class="fine" x="70" y="106">(Pleiospilos nelii)</text>
    <text class="fine-head" x="6" y="118">AUSSAAT</text>
    <text class="fine" x="6" y="124">Samen fein streuen und leicht</text>
    <text class="fine" x="6" y="129">mit Wasser besprühen.</text>
    <text class="fine-head" x="6" y="139">KEIMUNG</text>
    <text class="fine" x="6" y="145">Bei Wärme keimen die Samen</text>
    <text class="fine" x="6" y="150">schon nach wenigen Tagen.</text>
    <text class="fine-head" x="6" y="160">PFLEGE</text>
    <text class="fine" x="6" y="166">Im Winter kühl und trocken</text>
    <text class="fine" x="6" y="171">halten, kaum gießen.</text>
    <text class="fine" x="6" y="232">Sprosslabor GmbH · Musterweg 12 · 10115 Berlin</text>
    <circle class="brand-dot" cx="92" cy="240" r="2.5"/>
    <text class="brand" x="64" y="242" font-size="5">Sprosslabor</text>
  </g>
</svg>

</body>
</html>
```